Intenational Rhythmic Gymnastics Frostline Trophy

We need a poster for our new annual international rhythmic gymnastics competition "Frostline Trophy". Dates are December 21 -23, 2019.Picture we would like to use is attached.We would like to see holidays colors in the poster.It should have words "international rhythmic gymnastics", Name of the competition "Frostline Trophy" and dates.Also we would like for it to say somewhere that it is in Los Angeles, California, USAIt should have information about our club on the bottom of the poster like on the file attached (hosted by Venmarra Gymnastics with logo and address and website info)We also need a flyer that ties into the poster in look and colors with empty space below so we can add directives.We would like end product to be in file format that we can edit next year when the dates change.

Target Market(s)

Rhythmic Gymnastics Clubs

Industry/Entity Type

Gym

Colors

Designer to choose colors to be used in the design.

Requirements
Must have
• Picture we uploaded and all info we requested.
• Bright holiday colors

```html
<!DOCTYPE html>
<html lang="en">
<head>
<meta charset="utf-8">
<title>International Rhythmic Gymnastics Frostline Trophy</title>
<link rel="stylesheet" href="https://fonts.googleapis.com/css2?family=Open+Sans:wght@700;800&family=Roboto:wght@400;500;700&family=Roboto+Condensed:wght@400;700&family=Kaushan+Script&family=Libre+Baskerville&display=swap">
<style>
  :root {
    --page-bg: #d9dadc;
    --night: #15162e;
    --deep-blue: #1c3f8a;
    --stage-blue: #1f8fd6;
    --ice-blue: #86d3f3;
    --frost: #eef6fb;
    --white: #ffffff;
    --gold-light: #fff6d8;
    --gold: #e8c46a;
    --gold-dark: #a9802c;
    --ink: #14173a;
    --magenta: #b0399a;
    --navy: #1f2560;
    --muted: #3a3d55;
    --leotard-violet: #5a4a9a;
    --skin-gold: #d9b48a;
  }
  * { margin: 0; padding: 0; box-sizing: border-box; }
  html, body {
    width: 1200px; height: 1200px; overflow: hidden;
    background: var(--page-bg);
  }
  .poster {
    position: absolute; left: 138px; top: 0;
    width: 924px; height: 1200px;
    background: var(--white);
    overflow: hidden;
  }
  .stage-backdrop {
    position: absolute; left: 0; top: 0;
    width: 924px; height: 1060px;
    background: linear-gradient(180deg,
      var(--night) 0%, #1b2350 20%, var(--deep-blue) 38%,
      var(--stage-blue) 58%, var(--ice-blue) 78%, var(--frost) 95%, var(--white) 100%);
  }
  .gymnast-photo {
    position: absolute; left: 150px; top: 440px;
    width: 680px; height: 560px;
    border-radius: 40% 40% 30% 30% / 50% 50% 20% 20%;
    background:
      radial-gradient(ellipse 30% 40% at 58% 60%, rgba(90, 74, 154, 0.85), rgba(90, 74, 154, 0) 100%),
      radial-gradient(ellipse 50% 30% at 60% 82%, rgba(217, 180, 138, 0.75), rgba(217, 180, 138, 0) 100%),
      radial-gradient(ellipse 35% 45% at 35% 35%, rgba(40, 50, 140, 0.7), rgba(40, 50, 140, 0) 100%),
      radial-gradient(ellipse 60% 50% at 50% 50%, rgba(255, 255, 255, 0.45), rgba(255, 255, 255, 0) 100%);
  }
  .headline { position: absolute; left: 0; width: 100%; text-align: center; }
  .gold-text {
    background: linear-gradient(180deg, var(--gold-light) 0%, var(--gold) 55%, var(--gold-dark) 100%);
    -webkit-background-clip: text; background-clip: text;
    color: transparent;
  }
  .kicker {
    top: 60px;
    font-family: "Roboto", sans-serif; font-weight: 400;
    font-size: 32px; letter-spacing: 25px; padding-left: 25px;
    color: var(--gold);
  }
  .rhythmic {
    top: 104px;
    font-family: "Open Sans", sans-serif; font-weight: 800;
    font-size: 76px; letter-spacing: 9px; line-height: 1;
  }
  .gymnastics {
    top: 172px;
    font-family: "Open Sans", sans-serif; font-weight: 800;
    font-size: 114px; letter-spacing: -2px; line-height: 1;
  }
  .event-name {
    position: absolute; left: 262px; top: 300px;
    font-family: "Kaushan Script", cursive; font-weight: 400;
    font-size: 72px; line-height: 1; color: var(--white);
    transform: rotate(-5deg); transform-origin: left center;
    text-shadow: 0 3px 6px rgba(10, 20, 60, 0.5);
    white-space: nowrap;
  }
  .swoosh { position: absolute; left: 380px; top: 404px; }
  .dates {
    position: absolute; left: 384px; width: 230px; top: 444px;
    text-align: center; color: var(--ink);
    font-family: "Roboto Condensed", sans-serif; line-height: 1.3;
  }
  .dates .month { font-size: 36px; font-weight: 400; display: block; }
  .dates .days { font-size: 36px; font-weight: 700; display: block; }
  .footer {
    position: absolute; left: 0; top: 1060px; width: 100%; height: 140px;
  }
  .host { position: absolute; left: 58px; top: 20px; text-align: center; }
  .host .label {
    font-family: "Roboto", sans-serif; font-weight: 500;
    font-size: 12px; letter-spacing: 3px; color: var(--muted);
  }
  .host .club {
    display: flex; align-items: center; gap: 10px; margin-top: 8px;
    font-family: "Roboto", sans-serif; font-weight: 500;
    font-size: 24px; color: var(--navy);
  }
  .host .club .dot {
    width: 14px; height: 14px; border-radius: 50%; background: var(--navy);
  }
  .contact { position: absolute; left: 382px; top: 26px; text-align: center; width: 460px; }
  .contact .place {
    font-family: "Roboto", sans-serif; font-size: 20px;
    letter-spacing: 1px; color: var(--magenta);
  }
  .contact .web {
    margin-top: 12px;
    font-family: "Libre Baskerville", serif; font-size: 21px;
    letter-spacing: 5px; color: var(--navy);
  }
</style>
</head>
<body>
  <main class="poster">
    <div class="stage-backdrop" role="img" aria-label="Photo of a bright arena stage with blue spotlight beams crossing over a white floor"></div>
    <div class="gymnast-photo" role="img" aria-label="Photo of a rhythmic gymnast in a sparkling purple and gold leotard lunging on the stage, arm raised, waving a dark blue ribbon"></div>

    <p class="headline kicker gold-text">INTERNATIONAL</p>
    <h1 class="headline rhythmic gold-text">RHYTHMIC</h1>
    <p class="headline gymnastics gold-text">GYMNASTICS</p>

    <h2 class="event-name">Frostline Trophy</h2>
    <svg class="swoosh" width="420" height="40" viewBox="0 0 420 40" aria-hidden="true">
      <path d="M0 30 Q 200 2 410 16 L 410 22 Q 200 10 0 34 Z" fill="var(--white)"/>
    </svg>

    <div class="dates">
      <span class="month">DECEMBER</span>
      <span class="days">21 -23, 2019</span>
    </div>

    <footer class="footer">
      <div class="host">
        <p class="label">HOSTED BY</p>
        <p class="club"><span>Venmarra Gymnastics</span><span class="dot"></span></p>
      </div>
      <div class="contact">
        <p class="place">Los Angeles, California, USA</p>
        <p class="web">www.Venmarragymnastics.com</p>
      </div>
    </footer>
  </main>
</body>
</html>
```